Business Card Design for Bright Canvas Hue Designs

I need a business card design for Artist Marlon Ketch who specializes in Digital Fine Art, Digital Illustration, Murals and Mixed Media. Digital art techniques combine the use of a computer and specialized programs coupled with the same methods and theories used to produce traditional art. The final design should use the new logo that was just deigned and reflect an artist who has embraced the evolution of art by using modern technology to paint vibrant, stunning and high quality art. Please make this a double sided card and use the attached photo on the back of the card. Please include the name of the business: Bright Canvas Hue Designs, Artist: Marlon Ketch, Phone: 555-283-7190 Website: brightcanvashuedesigns.example

Target Market(s)

Anyone looking for fine art for there home or business.

Industry/Entity Type

Computer

Contact Information for Business Card

This should be a double sided business card with a modern feel to it.

Font styles to use
Sans Serif

Requirements
Must have
• Artist Name: Marlon Ketch
• Business Name and Logo: Bright Canvas Hue Designs
• Phone: 555-283-7190
• Website: brightcanvashuedesigns.example
• specializes in Digital Fine Art, Digital Illustration, Murals and Mixed Media
Nice to have
• Black background with new logo that is attached to file

```html
<!DOCTYPE html>
<html lang="en">
<head>
<meta charset="utf-8">
<title>Bright Canvas Hue Designs – Business Card</title>
<link rel="stylesheet" href="https://fonts.googleapis.com/css2?family=Arimo:wght@400;700&family=Exo+2:wght@600&display=swap">
<style>
  :root {
    --backdrop: #eee8da;
    --card-black: #050606;
    --ink-blue: #3a3996;
    --band-yellow: #e3d23c;
    --band-text: #0b0b0b;
    --divider: #cfcfcf;
    --art-gold: #f2c525;
    --art-orange: #ec8a2c;
    --art-teal: #49b8d6;
  }
  html, body {
    margin: 0;
    padding: 0;
    width: 1095px;
    height: 1200px;
    overflow: hidden;
    background: var(--backdrop);
  }
  .card {
    position: absolute;
    width: 900px;
    height: 528px;
    background: var(--card-black);
    overflow: hidden;
  }
  .card--front { left: 46px; top: 46px; }
  .card--back { left: 126px; top: 607px; }

  .brand-mark {
    position: absolute;
    left: 194px;
    top: 140px;
    width: 100px;
    height: 100px;
    border-radius: 50%;
    background: var(--ink-blue);
  }
  .brand-name {
    position: absolute;
    left: 24px;
    width: 440px;
    top: 300px;
    margin: 0;
    text-align: center;
    font-family: "Exo 2", sans-serif;
    font-weight: 600;
    font-size: 29px;
    color: var(--ink-blue);
  }
  .divider {
    position: absolute;
    left: 452px;
    top: 103px;
    width: 2px;
    height: 258px;
    background: var(--divider);
  }
  .artist-name {
    position: absolute;
    left: 515px;
    top: 160px;
    margin: 0;
    font-family: "Arimo", sans-serif;
    font-weight: 400;
    font-size: 37px;
    color: var(--ink-blue);
  }
  .artist-role {
    position: absolute;
    left: 516px;
    top: 216px;
    margin: 0;
    font-family: "Arimo", sans-serif;
    font-size: 22px;
    letter-spacing: 2px;
    color: var(--ink-blue);
  }
  .phone {
    position: absolute;
    left: 515px;
    top: 298px;
    display: flex;
    align-items: center;
    gap: 18px;
    font-family: "Arimo", sans-serif;
    font-size: 20px;
    letter-spacing: 1.5px;
    color: var(--ink-blue);
  }
  .phone svg { width: 21px; height: 21px; display: block; }
  .specialties {
    position: absolute;
    left: 0;
    top: 412px;
    width: 100%;
    height: 36px;
    background: var(--band-yellow);
    display: flex;
    align-items: center;
    justify-content: center;
    font-family: "Arimo", sans-serif;
    font-weight: 700;
    font-size: 22px;
    letter-spacing: 0.6px;
    color: var(--band-text);
  }
  .website {
    position: absolute;
    left: 0;
    top: 478px;
    width: 100%;
    margin: 0;
    text-align: center;
    font-family: "Arimo", sans-serif;
    font-weight: 700;
    font-size: 20px;
    letter-spacing: 3.5px;
    color: var(--ink-blue);
  }
  .feature-art {
    position: absolute;
    left: 133px;
    top: 66px;
    width: 632px;
    height: 400px;
    border-radius: 46% 42% 48% 40% / 50% 46% 52% 48%;
    background:
      radial-gradient(ellipse at 40% 55%, var(--art-gold) 0%, var(--art-orange) 38%, transparent 62%),
      linear-gradient(120deg, var(--art-teal) 0%, #2f8fb0 100%);
  }
</style>
</head>
<body>
  <section class="card card--front">
    <div class="brand-mark"></div>
    <p class="brand-name">Bright Canvas Hue Designs</p>
    <div class="divider"></div>
    <p class="artist-name">Marlon Ketch</p>
    <p class="artist-role">Artist</p>
    <div class="phone">
      <svg viewBox="0 0 24 24" aria-hidden="true">
        <rect x="0" y="0" width="24" height="24" rx="5" fill="#3a3996"/>
        <path d="M8.2 5.5c.5-.3 1.1-.2 1.4.3l1.3 2.2c.3.5.2 1.1-.2 1.4l-1 .8c.7 1.6 1.9 2.9 3.5 3.7l.8-1c.4-.4 1-.5 1.4-.2l2.2 1.3c.5.3.6.9.3 1.4l-.9 1.4c-.4.6-1.1.9-1.8.7C10.9 16.4 7.6 13.1 6.5 8.9c-.2-.7.1-1.4.7-1.8z" fill="#050606"/>
      </svg>
      <span>555 283 7190</span>
    </div>
    <div class="specialties">Specializes in Digital Fine Art, Digital Illustration, Murals and Mixed Media</div>
    <p class="website">www.brightcanvashuedesigns.example</p>
  </section>

  <section class="card card--back">
    <div class="feature-art" role="img" aria-label="Artwork: a colourful golden-orange koi fish swimming among stylised turquoise waves"></div>
  </section>
</body>
</html>
```